"Bright Hollow Craft Dwellings" need a busines Card Design got Builder

We need a business card design for a company based in Milford, Michigancalled Bright Hollow Craft Dwellings - has been recognized as a premier custom home builder. Distinguished by outstanding craftmanship and timeless beauty. Our custom home can be found in the most prestigious communities in Michigan. The homes are built with ICF (insulated concrete homes) which is green, allergy free, fire free, mold free and quitter. Our slogan "shaping one home at a Time" and also we are ICF distributor for the state of Michigan

Target Market(s)

Anyone who is making over $100,000 a year and who wants to have totally custom built home. Ages from 29 up to 60 years old

Industry/Entity Type

Concrete

Contact Information for Business Card

we want to use - green, black, gray or blue colors - we want to look different with our business cards, because we built homes only with ICF, green, healthier and highly energy efficient homes.

Requirements
Must have
• I have logo that I attached and we have been using the logo (the only green home)
Nice to have
• should look quality business card,

```html
<!DOCTYPE html>
<html lang="en">
<head>
<meta charset="utf-8">
<title>Bright Hollow Craft Dwellings — Business Card</title>
<link rel="stylesheet" href="https://fonts.googleapis.com/css2?family=Nunito+Sans:wght@300;400&display=swap">
<style>
  :root {
    --page-bg: #d9d9d6;
    --card-bg: #ffffff;
    --navy: #2a2580;
    --deep-navy: #2b1f6b;
    --sky: #1a8fe3;
    --name-gray: #8a8a8a;
    --card-shadow: rgba(0, 0, 0, 0.18);
  }
  * { margin: 0; padding: 0; box-sizing: border-box; }
  html, body {
    width: 1200px;
    height: 848px;
    overflow: hidden;
    background: var(--page-bg);
    font-family: "Nunito Sans", Arial, sans-serif;
  }
  .business-card {
    position: absolute;
    left: 100px;
    top: 138px;
    width: 1000px;
    height: 572px;
    background: var(--card-bg);
    border-radius: 40px;
    box-shadow: 0 12px 36px var(--card-shadow);
  }
  .brand {
    position: absolute;
    left: 64px;
    top: 52px;
    display: flex;
    align-items: center;
    gap: 26px;
  }
  .brand-dot {
    width: 104px;
    height: 104px;
    border-radius: 50%;
    background: var(--deep-navy);
    flex: none;
  }
  .brand-name {
    font-weight: 300;
    font-size: 34px;
    line-height: 1.0;
    letter-spacing: 3px;
    text-transform: uppercase;
    color: var(--name-gray);
  }
  .tagline {
    position: absolute;
    left: 64px;
    top: 200px;
    color: var(--navy);
  }
  .tagline-main {
    font-weight: 400;
    font-size: 27px;
    line-height: 1.1;
  }
  .tagline-sub {
    font-weight: 400;
    font-size: 17px;
    line-height: 1.3;
  }
  .contact-list {
    position: absolute;
    left: 64px;
    top: 318px;
    list-style: none;
    color: var(--navy);
    font-weight: 300;
    font-size: 27px;
    line-height: 1.45;
  }
  .contact-item {
    display: flex;
    align-items: center;
    gap: 16px;
  }
  .contact-icon {
    width: 20px;
    height: 22px;
    flex: none;
    fill: var(--sky);
  }
</style>
</head>
<body>
  <article class="business-card">
    <header class="brand">
      <span class="brand-dot"></span>
      <h1 class="brand-name">Bright Hollow<br>Craft Dwellings</h1>
    </header>

    <section class="tagline">
      <p class="tagline-main">shaping one home at a Time</p>
      <p class="tagline-sub">crafting Insulated Concrete Form (ICF) homes since 2004</p>
    </section>

    <ul class="contact-list">
      <li class="contact-item">
        <svg class="contact-icon" viewBox="0 0 20 22" aria-hidden="true">
          <path d="M6 1 C3 2 1 6 2 11 C3 16 7 20 11 21 L13 17 L10 15 C8 14 7 10 8 7 L11 6 L10 2 Z"/>
        </svg>
        <span>555-301-2748</span>
      </li>
      <li class="contact-item">
        <svg class="contact-icon" viewBox="0 0 20 22" aria-hidden="true">
          <path d="M6 1 C3 2 1 6 2 11 C3 16 7 20 11 21 L13 17 L10 15 C8 14 7 10 8 7 L11 6 L10 2 Z"/>
        </svg>
        <span>555-418-6093</span>
      </li>
      <li class="contact-item">
        <svg class="contact-icon" viewBox="0 0 20 22" aria-hidden="true">
          <path d="M10 1 C5 1 2 4.5 2 8.5 C2 14 10 21 10 21 C10 21 18 14 18 8.5 C18 4.5 15 1 10 1 Z M10 5.5 A3 3 0 1 1 10 11.5 A3 3 0 1 1 10 5.5 Z" fill-rule="evenodd"/>
        </svg>
        <span>27 Cedar Ridge Lane #112, Alderbrook, OR 97000, United States</span>
      </li>
    </ul>
  </article>
</body>
</html>
```